Electrical business needs a flyer design

we need a Trifold flyer designed for an electrical company. Our service include new installations, renovations and rewires, safety checks, switchboard upgrades, services and breakdown, home automation and power monitoring. we would like to see designs using dark grey, orange and blue. the final designs should communicate a friendly but professional service. I have attached my old business brochure to indicate the service we provide
Target Market(s)
home owners
Industry/Entity Type
Electrical
Look and feel
Each slider illustrates characteristics of the customer's brand and the style your logo design should communicate.

```html
<!DOCTYPE html>
<html lang="en">
<head>
<meta charset="utf-8">
<title>Crestline Electrical – Trifold Brochure</title>
<link href="https://fonts.googleapis.com/css2?family=Montserrat:wght@400;500;600;700;800&display=swap" rel="stylesheet">
<style>
:root{
  --blue:#1f74bd;
  --navy:#123f5c;
  --navy-deep:#0e3149;
  --orange:#f27522;
  --ink:#2b2b2b;
  --grey-dark:#4a4a4a;
  --page:#ffffff;
  --bg:#eeeeee;
  --line:#9ec3e4;
}
*{box-sizing:border-box;margin:0;padding:0}
html,body{width:687px;height:1200px;overflow:hidden;background:var(--bg);font-family:"Montserrat",sans-serif;color:var(--ink)}
.canvas{position:relative;width:687px;height:1200px}
.spread{position:absolute;left:13px;width:661px;height:468px;background:var(--page);box-shadow:0 2px 6px rgba(0,0,0,.18);overflow:hidden}
.spread--outside{top:110px}
.spread--inside{top:622px}
.panel{position:absolute;top:0;width:220.33px;height:100%}
.panel--1{left:0}.panel--2{left:220.33px}.panel--3{left:440.66px}

.tag{position:absolute;left:23px;right:23px;height:11px;border-top:1px solid var(--line)}
.tag span{display:inline-block;background:var(--blue);color:#fff;font-weight:600;font-size:7px;letter-spacing:.3px;padding:1.5px 16px 1.5px 5px;clip-path:polygon(0 0,100% 0,calc(100% - 8px) 100%,0 100%);line-height:1.15}
.tag--orange span{background:var(--orange)}
.body{position:absolute;left:23px;right:23px;font-size:5.9px;line-height:1.6;text-align:justify;color:#333}

.photo{position:absolute}
.photo--worker{left:0;right:0;top:236px;bottom:0;background:linear-gradient(180deg,#ffffff 0%,#ececec 35%,#d8d6d2 100%)}
.photo--worker::after{content:"";position:absolute;left:95px;top:10px;width:90px;bottom:0;background:radial-gradient(ellipse at 50% 45%,rgba(120,120,125,.45),rgba(120,120,125,0) 70%)}

.band{position:absolute;left:0;top:0;width:100%;height:227px;background:linear-gradient(180deg,var(--navy-deep) 0%,var(--navy) 60%,#2a5f7e 100%);border-bottom:3px solid var(--orange)}
.brand{position:absolute;top:34px;left:0;right:0;text-align:center;color:#fff}
.brand__name{display:inline-flex;align-items:center;gap:5px;font-weight:600;font-size:11.5px;letter-spacing:.2px}
.brand__dot{width:9px;height:9px;border-radius:50%;border:1.5px solid #fff}
.brand__sub{font-size:4.6px;letter-spacing:2.2px;margin-top:3px;font-weight:500}

.phone-big{position:absolute;left:23px;font-weight:700;font-size:15px;color:#222;display:flex;align-items:center;gap:6px}
.contact-line{position:absolute;left:23px;font-size:6.4px;display:flex;align-items:center;gap:8px;color:#333}
.contact-line svg{width:7px;height:7px}

.cover-frame{position:absolute;left:20px;width:176px;top:120px;height:200px;background:#fff;border:5px solid #fff;box-shadow:0 1px 3px rgba(0,0,0,.2)}
.cover-frame::after{content:"";position:absolute;left:-5px;right:-5px;bottom:-5px;height:100px;border:4px solid var(--blue);border-top:none;pointer-events:none}
.photo--lineman{position:absolute;inset:0;background:linear-gradient(160deg,#c9ced4 0%,#9aa1a8 45%,#6d6456 75%,#a88a5c 100%)}
.warn{position:absolute;left:68px;top:280px;width:60px;height:52px}
.cover-title{position:absolute;left:0;right:0;top:342px;text-align:center;font-weight:700;line-height:.98}
.cover-title .t1{color:var(--blue);font-size:23px;letter-spacing:.5px}
.cover-title .t2{color:var(--orange);font-size:22.5px;letter-spacing:.3px}
.cover-tagline{position:absolute;left:0;right:0;top:398px;text-align:center;font-size:7.4px;font-weight:500}
.cover-tagline span{display:inline-block;padding-bottom:3px;border-bottom:1px solid #555}
.web-line{position:absolute;left:0;right:0;top:443px;text-align:center;font-size:6.4px;font-weight:600}

.photo--crew{position:absolute;left:0;top:0;width:441px;height:223px;background:linear-gradient(180deg,#b9c2c6 0%,#d8c8a4 45%,#e6a24a 75%,#7b6a48 100%);border-bottom:2px solid var(--orange)}
.cta{position:absolute;left:0;top:0;width:100%;height:240px;background:var(--blue);border-bottom-left-radius:10px;color:#fff}
.cta__head{position:absolute;left:23px;top:28px;font-weight:800;font-size:17.5px;color:var(--orange);letter-spacing:.2px}
.cta__phone{position:absolute;left:23px;top:48px;font-weight:700;font-size:19px}
.cta__quote{position:absolute;left:23px;top:74px;font-weight:500;font-size:11px;line-height:1.45}
.cta .tag{top:112px;border-top-color:rgba(255,255,255,.5)}
.cta .body{top:131px;color:#fff}
.photo--bulb{position:absolute;left:0;right:0;top:240px;bottom:11px;background:radial-gradient(ellipse at 35% 45%,#f6e3a4 0%,#d9c98e 25%,#e7ead8 55%,#ffffff 90%)}

.svc-list{position:absolute;left:23px;right:10px;list-style:none}
.svc{position:absolute;left:0;display:flex;align-items:center;gap:9px;font-size:6.7px;font-weight:500;color:#222;line-height:1.3}
.svc svg{width:20px;height:20px;flex:none}
.footer{position:absolute;left:0;right:0;bottom:0;height:11px;background:var(--grey-dark)}
.footer__tab{position:absolute;left:242px;width:177px;bottom:0;height:22px;background:var(--grey-dark);border-radius:10px 10px 0 0;color:#fff;text-align:center;font-size:6.6px;font-weight:500;padding-top:6px}
</style>
</head>
<body>
<div class="canvas">

  <!-- Outside spread -->
  <section class="spread spread--outside">
    <div class="panel panel--1">
      <div class="tag" style="top:27px"><span>WE OFFER</span></div>
      <p class="body" style="top:44px">We offer a 24-hour, seven-day emergency response service where you need an electrician due to a break-down or other disruption to your power supply. Our electrical contractors will identify the fault and have your power back on as soon as possible.</p>
      <div class="tag" style="top:106px"><span>ACCREDITED MASTER<br>ELECTRICIAN</span></div>
      <p class="body" style="top:139px">Electrical work is one of the most dangerous tasks that can be performed in a home or business. Every year, dozens of people are electrocuted or shocked by substandard electrical work. By choosing a Master Electrician, you are choosing a contractor whose safety systems are accredited and monitored, and who provides a workmanship guarantee. Master Electricians are reliable contractors who provide excellent services and information, potentially saving you time and money.</p>
      <div class="photo photo--worker" role="img" aria-label="Photo of an electrician in a yellow hard hat holding a clipboard"></div>
    </div>

    <div class="panel panel--2">
      <div class="band" role="img" aria-label="Dark blue toned photo of power transmission towers">
        <div class="brand">
          <div class="brand__name"><span class="brand__dot"></span>CRESTLINE ELECTRICAL</div>
          <div class="brand__sub">MANAGEMENT &amp; AUTOMATION</div>
        </div>
      </div>
      <div class="tag" style="top:239px"><span>ABOUT US</span></div>
      <p class="body" style="top:256px">Crestline Electrical is a privately owned business providing a comprehensive range of domestic, commercial and industrial electrical services.</p>
      <p class="body" style="top:292px">We provide a comprehensive range of electrical and communication services including small jobs around the home to large industrial applications. Our business is underpinned by a commitment to customer service, that is, we turn up on time providing quality workmanship at a fair and competitive price.</p>
      <div class="tag" style="top:362px"><span>CONTACT INFORMATION</span></div>
      <div class="phone-big" style="top:378px">
        <svg width="10" height="10" viewBox="0 0 24 24"><path fill="#1f74bd" d="M6.6 10.8c1.4 2.8 3.8 5.1 6.6 6.6l2.2-2.2c.3-.3.7-.4 1-.2 1.1.4 2.3.6 3.6.6.6 0 1 .4 1 1V20c0 .6-.4 1-1 1C10.6 21 3 13.4 3 4c0-.6.4-1 1-1h3.5c.6 0 1 .4 1 1 0 1.3.2 2.5.6 3.6.1.3 0 .7-.2 1z"/></svg>
        555-218-4470
      </div>
      <div class="contact-line" style="top:403px"><svg viewBox="0 0 24 24"><rect x="2" y="5" width="20" height="14" fill="#1f74bd"/><path d="M2 5l10 8 10-8" stroke="#fff" stroke-width="2" fill="none"/></svg>info@crestlineelectrical.com</div>
      <div class="contact-line" style="top:418px"><svg viewBox="0 0 24 24"><rect x="4" y="9" width="16" height="10" fill="#1f74bd"/><rect x="7" y="3" width="10" height="6" fill="#1f74bd"/></svg>55512840</div>
      <div class="contact-line" style="top:433px"><svg viewBox="0 0 24 24"><circle cx="12" cy="12" r="9" fill="none" stroke="#1f74bd" stroke-width="2.5"/><path d="M3 12h18M12 3c-4 5-4 13 0 18M12 3c4 5 4 13 0 18" stroke="#1f74bd" stroke-width="1.6" fill="none"/></svg>crestlineelectrical.com</div>
    </div>

    <div class="panel panel--3">
      <div class="band" role="img" aria-label="Dark blue toned photo of power transmission towers">
        <div class="brand">
          <div class="brand__name"><span class="brand__dot"></span>CRESTLINE ELECTRICAL</div>
          <div class="brand__sub">MANAGEMENT &amp; AUTOMATION</div>
        </div>
      </div>
      <div class="cover-frame">
        <div class="photo--lineman" role="img" aria-label="Photo of linemen in hard hats working on a utility pole"></div>
      </div>
      <svg class="warn" viewBox="0 0 60 52">
        <path d="M30 3 L57 49 H3 Z" fill="#fff" stroke="#1f74bd" stroke-width="4" stroke-linejoin="round"/>
        <path d="M33 17 L24 33 H30 L27 43 L37 27 H31 Z" fill="#f27522"/>
      </svg>
      <div class="cover-title"><div class="t1">CRESTLINE</div><div class="t2">ELECTRICAL</div></div>
      <div class="cover-tagline"><span>Management &amp; Automation</span></div>
      <div class="web-line">www.crestlineelectrical.com</div>
    </div>
  </section>

  <!-- Inside spread -->
  <section class="spread spread--inside">
    <div class="photo--crew" role="img" aria-label="Photo of two electricians in hard hats and safety vests looking at a transmission tower at sunset"></div>

    <div class="panel panel--1">
      <div class="tag" style="top:243px"><span>ELECTRICAL SERVICES</span></div>
      <ul class="svc-list">
        <li class="svc" style="top:262px"><svg viewBox="0 0 20 20"><circle cx="10" cy="10" r="8.5" fill="none" stroke="#bbb" stroke-dasharray="1.5 1.5"/><path d="M10 1.5 A8.5 8.5 0 0 1 18.5 10" fill="none" stroke="#f27522" stroke-width="1.3"/><path d="M6 10 L10 6.5 L14 10 V14 H6 Z" fill="none" stroke="#555" stroke-width=".9"/></svg>New Installations</li>
        <li class="svc" style="top:298px"><svg viewBox="0 0 20 20"><circle cx="10" cy="10" r="8.5" fill="none" stroke="#bbb" stroke-dasharray="1.5 1.5"/><path d="M10 1.5 A8.5 8.5 0 0 1 18.5 10" fill="none" stroke="#f27522" stroke-width="1.3"/><path d="M6 6 L14 14 M14 6 L6 14" stroke="#555" stroke-width="1.1"/></svg>Renovations and re-Wiring</li>
        <li class="svc" style="top:337px"><svg viewBox="0 0 20 20"><circle cx="10" cy="10" r="8.5" fill="none" stroke="#bbb" stroke-dasharray="1.5 1.5"/><path d="M10 1.5 A8.5 8.5 0 0 1 18.5 10" fill="none" stroke="#f27522" stroke-width="1.3"/><rect x="7.5" y="5.5" width="5" height="9" fill="none" stroke="#555" stroke-width=".9"/><rect x="9" y="7.5" width="2" height="3" fill="#555"/></svg>Installation of Safety Switches</li>
        <li class="svc" style="top:377px"><svg viewBox="0 0 20 20"><circle cx="10" cy="10" r="8.5" fill="none" stroke="#bbb" stroke-dasharray="1.5 1.5"/><path d="M10 1.5 A8.5 8.5 0 0 1 18.5 10" fill="none" stroke="#f27522" stroke-width="1.3"/><rect x="6" y="6" width="8" height="8" fill="none" stroke="#555" stroke-width=".9"/><path d="M8 8v4M10 8v4M12 8v4" stroke="#555" stroke-width=".8"/></svg>Switchboard Upgrades</li>
        <li class="svc" style="top:416px"><svg viewBox="0 0 20 20"><circle cx="10" cy="10" r="8.5" fill="none" stroke="#bbb" stroke-dasharray="1.5 1.5"/><path d="M10 1.5 A8.5 8.5 0 0 1 18.5 10" fill="none" stroke="#f27522" stroke-width="1.3"/><circle cx="10" cy="8" r="2" fill="none" stroke="#555" stroke-width=".9"/><path d="M6.5 14.5c0-2.5 7-2.5 7 0" fill="none" stroke="#555" stroke-width=".9"/></svg>Services and Break Downs</li>
      </ul>
    </div>

    <div class="panel panel--2">
      <div class="tag" style="top:243px"><span>COMMUNICATION SERVICE</span></div>
      <ul class="svc-list">
        <li class="svc" style="top:268px"><svg viewBox="0 0 20 20"><circle cx="10" cy="10" r="8.5" fill="none" stroke="#bbb" stroke-dasharray="1.5 1.5"/><path d="M10 1.5 A8.5 8.5 0 0 1 18.5 10" fill="none" stroke="#f27522" stroke-width="1.3"/><path d="M6 10 L10 6.5 L14 10 V14 H6 Z" fill="none" stroke="#555" stroke-width=".9"/></svg>New Installations</li>
        <li class="svc" style="top:298px"><svg viewBox="0 0 20 20"><circle cx="10" cy="10" r="8.5" fill="none" stroke="#bbb" stroke-dasharray="1.5 1.5"/><path d="M10 1.5 A8.5 8.5 0 0 1 18.5 10" fill="none" stroke="#f27522" stroke-width="1.3"/><rect x="6" y="8" width="8" height="6" rx="1" fill="none" stroke="#555" stroke-width=".9"/><circle cx="10" cy="11" r="1.5" fill="none" stroke="#555" stroke-width=".8"/></svg>Additional Phone and<br>Data Points</li>
        <li class="svc" style="top:339px"><svg viewBox="0 0 20 20"><circle cx="10" cy="10" r="8.5" fill="none" stroke="#bbb" stroke-dasharray="1.5 1.5"/><path d="M10 1.5 A8.5 8.5 0 0 1 18.5 10" fill="none" stroke="#f27522" stroke-width="1.3"/><rect x="5.5" y="8" width="9" height="6" fill="none" stroke="#555" stroke-width=".9"/><path d="M8 5l2 3 2-3" fill="none" stroke="#555" stroke-width=".8"/></svg>Antennas and TV Points</li>
        <li class="svc" style="top:378px"><svg viewBox="0 0 20 20"><circle cx="10" cy="10" r="8.5" fill="none" stroke="#bbb" stroke-dasharray="1.5 1.5"/><path d="M10 1.5 A8.5 8.5 0 0 1 18.5 10" fill="none" stroke="#f27522" stroke-width="1.3"/><rect x="5.5" y="6" width="4" height="4" fill="none" stroke="#555" stroke-width=".8"/><rect x="10.5" y="10" width="4" height="4" fill="none" stroke="#555" stroke-width=".8"/><path d="M9.5 8h3v2" fill="none" stroke="#555" stroke-width=".8"/></svg>LAN Setups</li>
      </ul>
    </div>

    <div class="panel panel--3">
      <div class="cta">
        <div class="cta__head">CALL US TODAY</div>
        <div class="cta__phone">555-218-4470</div>
        <div class="cta__quote">FOR A FREE<br>NO OBLIGATION QUOTE</div>
        <div class="tag tag--orange"><span>OUR PHILOSOPHY</span></div>
        <p class="body">Crestline electrical focuses on providing our customers with the best possible service available. Our trades people are highly qualified to ensure quality and reliability. We strive to continually change and grow within the industry. We are constantly making changes to serve you better.</p>
      </div>
      <div class="photo--bulb" role="img" aria-label="Photo of glowing light bulbs on a soft pale background"></div>
    </div>

    <div class="footer"></div>
    <div class="footer__tab">www.crestlineelectrical.com</div>
  </section>

</div>
</body>
</html>
```